Redesign Colorful Business Card

Please redesign the card attached. It is too busy. Please don't eliminate any of the words. The repetivite word "free" can be used less often.

Target Market(s)

College Students.

Contact Information for Business Card

The details listed in the attached image

Font styles to use
Sans Serif

Requirements
Must have
• A clear and simple presentation and must be attractive.

```html
<!DOCTYPE html>
<html lang="en">
<head>
<meta charset="utf-8">
<title>StudyNimbl.com Business Card</title>
<link rel="stylesheet" href="https://fonts.googleapis.com/css2?family=Jost:wght@400;500;600&display=swap">
<style>
  :root {
    --stage: #3d3d40;
    --paper: #ffffff;
    --paper-shade: #e6e7ea;
    --ink-dark: #0d0d0d;
    --ink-light: #ffffff;
    --blue: #2e3a92;
    --purple: #a0449a;
    --green: #6bb431;
    --yellow: #f4e217;
    --cyan: #6ec7d9;
    --cream: #f3e6b0;
    --red: #e0262a;
  }
  * { box-sizing: border-box; margin: 0; padding: 0; }
  html, body { width: 1200px; height: 801px; overflow: hidden; }
  body {
    background: var(--stage);
    font-family: "Jost", sans-serif;
    position: relative;
  }
  .card {
    position: absolute;
    top: 245px;
    width: 540px;
    height: 310px;
    border-radius: 18px;
    overflow: hidden;
  }
  /* Front */
  .card-front {
    left: 40px;
    background: radial-gradient(ellipse at 65% 45%, var(--paper) 0%, var(--paper-shade) 100%);
  }
  .front-brand {
    position: absolute;
    left: 28px;
    top: 40px;
    width: 200px;
    height: 230px;
    display: flex;
    flex-direction: column;
    justify-content: flex-end;
  }
  .brand-dot {
    width: 120px;
    height: 120px;
    border-radius: 50%;
    background: linear-gradient(180deg, var(--red), var(--purple), var(--blue), var(--cyan));
    margin: 0 auto 22px;
  }
  .brand-name {
    font-weight: 500;
    font-size: 30px;
    letter-spacing: -0.5px;
    line-height: 1;
  }
  .card-front .brand-name { color: var(--ink-dark); }
  .benefits {
    position: absolute;
    left: 250px;
    top: 36px;
    list-style: none;
    display: flex;
    flex-direction: column;
    gap: 22px;
  }
  .benefit {
    display: flex;
    align-items: flex-start;
    gap: 10px;
    font-weight: 500;
    font-size: 17px;
    line-height: 1.05;
    text-transform: uppercase;
  }
  .badge-free {
    flex: none;
    background: var(--yellow);
    color: var(--ink-dark);
    font-size: 11px;
    font-weight: 600;
    padding: 3px 7px;
    border-radius: 9px 9px 9px 2px;
    margin-top: 6px;
  }
  .benefit-blue { color: var(--blue); }
  .benefit-purple { color: var(--purple); }
  .benefit-green { color: var(--green); }
  /* Back */
  .card-back {
    left: 620px;
    background: var(--ink-dark);
  }
  .back-brand {
    position: absolute;
    left: 34px;
    top: 70px;
    width: 220px;
    text-align: center;
  }
  .back-brand .brand-dot { width: 90px; height: 90px; margin-bottom: 18px; }
  .card-back .brand-name { color: var(--ink-light); font-size: 28px; }
  .rainbow-rule {
    position: absolute;
    left: 280px;
    top: 70px;
    width: 2px;
    height: 170px;
    background: linear-gradient(180deg, var(--red), #f29a1b, var(--yellow), var(--green), var(--blue), var(--purple), var(--red));
  }
  .contact {
    position: absolute;
    left: 302px;
    top: 82px;
  }
  .person-name {
    color: var(--cyan);
    font-size: 27px;
    font-weight: 500;
    line-height: 1;
  }
  .person-title {
    color: var(--cream);
    font-size: 13px;
    margin-top: 4px;
  }
  .contact-list {
    list-style: none;
    margin-top: 22px;
    display: flex;
    flex-direction: column;
    gap: 6px;
  }
  .contact-item {
    color: var(--cream);
    font-size: 15px;
    display: flex;
    align-items: center;
    gap: 8px;
  }
  .contact-item svg { width: 12px; height: 12px; flex: none; }
</style>
</head>
<body>
  <section class="card card-front">
    <div class="front-brand">
      <div class="brand-dot"></div>
      <span class="brand-name">StudyNimbl.com</span>
    </div>
    <ul class="benefits">
      <li class="benefit benefit-blue"><span class="badge-free">Free</span><span>Cut study time<br>down by<br>upto 50%</span></li>
      <li class="benefit benefit-purple"><span class="badge-free">Free</span><span>Learn a subject<br>without having to<br>go to class</span></li>
      <li class="benefit benefit-green"><span class="badge-free">Free</span><span>Memorize<br>anythig<br>quickly</span></li>
    </ul>
  </section>

  <section class="card card-back">
    <div class="back-brand">
      <div class="brand-dot"></div>
      <span class="brand-name">StudyNimbl.com</span>
    </div>
    <div class="rainbow-rule"></div>
    <div class="contact">
      <p class="person-name">Dorian Vale</p>
      <p class="person-title">Founder &amp; CEO</p>
      <ul class="contact-list">
        <li class="contact-item">
          <svg viewBox="0 0 12 12"><path d="M2 1h2.5l1 3-1.5 1a6 6 0 0 0 3 3l1-1.5 3 1V10a1 1 0 0 1-1 1A9 9 0 0 1 1 2a1 1 0 0 1 1-1z" fill="var(--red)"/></svg>
          555-014-2738
        </li>
        <li class="contact-item">
          <svg viewBox="0 0 12 12"><rect x="0.5" y="2" width="11" height="8" fill="var(--green)"/><path d="M0.5 2l5.5 4.5L11.5 2" stroke="var(--ink-dark)" fill="none"/></svg>
          info@StudyNimbl.com
        </li>
        <li class="contact-item">
          <svg viewBox="0 0 12 12"><circle cx="6" cy="6" r="5.5" fill="var(--purple)"/><path d="M0.5 6h11M6 0.5c-3 3-3 8 0 11M6 0.5c3 3 3 8 0 11" stroke="var(--ink-dark)" stroke-width="0.8" fill="none"/></svg>
          StudyNimbl.com
        </li>
      </ul>
    </div>
  </section>
</body>
</html>
```